Business Card Design (NEW FILES)

ATTENTION: New vector files are available. Please update your design to reflect/use the new (better resolution) logo images.

Seeking a unique and professional business card design for a commercial drone photography/videography business. The layout should feature
the logo (attached) and include the following information:
978-512-6037
www.skyvantmedia.com
ORD Certified Remote Pilot

```html
<!DOCTYPE html>
<html lang="en">
<head>
<meta charset="utf-8">
<title>Skyvant Media – Business Card</title>
<link rel="stylesheet" href="https://fonts.googleapis.com/css2?family=Montserrat:wght@400;500;700&display=swap">
<style>
  :root {
    --backdrop: #dcdcd8;
    --card: #ffffff;
    --navy: #161846;
    --orange: #e8834a;
    --ink: #1f1f2a;
    --edge: #e8834a;
  }
  * { box-sizing: border-box; margin: 0; padding: 0; }
  html, body {
    width: 1200px; height: 801px; overflow: hidden;
    background: var(--backdrop);
    font-family: "Montserrat", sans-serif;
  }
  .stage {
    position: relative; width: 1200px; height: 801px;
    display: flex; align-items: center; justify-content: center; gap: 50px;
  }
  .card {
    position: relative; width: 520px; height: 300px;
    background: var(--card); border-radius: 16px;
    border-bottom: 3px solid var(--edge);
    box-shadow: 0 10px 24px rgba(0,0,0,.18);
    overflow: hidden;
  }
  /* Contact side */
  .card-front .brand {
    position: absolute; left: 30px; top: 0; width: 200px; height: 100%;
    display: flex; align-items: center; justify-content: center; gap: 8px;
  }
  .brand-dot {
    width: 14px; height: 14px; border-radius: 50%; background: var(--orange); flex: none;
  }
  .brand-name {
    font-weight: 500; color: var(--navy); letter-spacing: .06em;
    text-transform: uppercase; font-size: 20px; line-height: 1.1;
  }
  .divider {
    position: absolute; left: 250px; top: 70px; width: 1.5px; height: 110px;
    background: var(--orange);
  }
  .contact { position: absolute; left: 276px; top: 64px; }
  .person-name { font-weight: 700; color: var(--orange); font-size: 26px; }
  .person-role { font-size: 15px; color: var(--ink); margin-top: 2px; }
  .contact-list { list-style: none; margin-top: 18px; }
  .contact-list li {
    display: flex; align-items: center; gap: 8px;
    font-size: 14px; color: var(--ink); margin-bottom: 7px;
  }
  .contact-list svg { width: 14px; height: 14px; flex: none; }
  .credentials {
    position: absolute; left: 0; right: 0; bottom: 34px;
    text-align: center; font-size: 15px; color: var(--ink);
  }
  /* Logo side */
  .card-back { border-bottom-color: #e2b12f; }
  .card-back .brand {
    position: absolute; inset: 0;
    display: flex; align-items: center; justify-content: center; gap: 16px;
  }
  .card-back .brand-dot { width: 26px; height: 26px; }
  .card-back .brand-name { font-size: 42px; }
</style>
</head>
<body>
<main class="stage">
  <section class="card card-front" aria-label="Business card, contact side">
    <div class="brand">
      <span class="brand-dot"></span>
      <span class="brand-name">Skyvant<br>Media</span>
    </div>
    <div class="divider"></div>
    <div class="contact">
      <h1 class="person-name">Mark Doyle</h1>
      <p class="person-role">Owner</p>
      <ul class="contact-list">
        <li>
          <svg viewBox="0 0 24 24" aria-hidden="true"><path fill="#e8834a" d="M6.6 10.8a15.1 15.1 0 0 0 6.6 6.6l2.2-2.2a1 1 0 0 1 1-.25 11.4 11.4 0 0 0 3.6.57 1 1 0 0 1 1 1V20a1 1 0 0 1-1 1A17 17 0 0 1 3 4a1 1 0 0 1 1-1h3.5a1 1 0 0 1 1 1c0 1.25.2 2.45.57 3.57a1 1 0 0 1-.25 1z"/></svg>
          978-512-6037
        </li>
        <li>
          <svg viewBox="0 0 24 24" aria-hidden="true"><circle cx="12" cy="12" r="10" fill="#e8834a"/><path d="M2 12h20M12 2c3 3 3 17 0 20M12 2c-3 3-3 17 0 20" stroke="#fff" stroke-width="1.4" fill="none"/></svg>
          www.skyvantmedia.com
        </li>
      </ul>
    </div>
    <p class="credentials">ORD Certified Remote Pilot Fully Insured</p>
  </section>

  <section class="card card-back" aria-label="Business card, brand side">
    <div class="brand">
      <span class="brand-dot"></span>
      <span class="brand-name">Skyvant Media</span>
    </div>
  </section>
</main>
</body>
</html>
```